Harbor Nightclub

Nightclub flyer., digital single sided, for KV and PX. I included samples of some previous flyers we've used. Sample Info:
HARBOR
FRIDAYS
FRI MAY 1 2020
DJ VORTAN (club floor)
DJ RUZO & DJ TAV (residents on the lounge floor)
4217 Marlow Avenue Sacramento
www.harborvenuehall.example for list/VIP inquiries

Target Market(s)

Upscale top 40 crowd but want some cool and artsy like the examples included.

Font styles to use
Sans Serif

Requirements
Must have
• Harbor Logo
Nice to have
• Would be nice if the flyer can be incorporated later with DJ photos (sometimes we will add dj photos to pixagram etc). Would like a big city type of feel.
Should not have
• Nothing too sexual.

```html
<!DOCTYPE html>
<html lang="en">
<head>
<meta charset="utf-8">
<title>Harbor Nightclub – Fridays</title>
<link rel="stylesheet" href="https://fonts.googleapis.com/css2?family=Oswald:wght@500;600&family=Raleway:wght@300;500;700;800&family=Open+Sans:ital,wght@1,400&family=Josefin+Sans:wght@700&display=swap">
<style>
  :root {
    --navy: #1b1a3c;
    --navy-deep: #14132e;
    --crimson: #c8234a;
    --crimson-soft: #a81f45;
    --gold: #f7c21a;
    --gold-deep: #f0a81b;
    --white: #ffffff;
    --mist: #c9cbe0;
  }
  * { margin: 0; padding: 0; box-sizing: border-box; }
  html, body { width: 856px; height: 1200px; overflow: hidden; background: var(--navy-deep); }
  .flyer {
    position: relative;
    width: 856px;
    height: 1200px;
    overflow: hidden;
    background: var(--navy);
    font-family: "Raleway", sans-serif;
    color: var(--white);
  }
  .backdrop { position: absolute; inset: 0; }

  .brand {
    position: absolute;
    left: 56px;
    top: 58px;
    width: 168px;
    text-align: center;
  }
  .brand-mark {
    width: 62px; height: 62px;
    margin: 0 auto 12px;
    border-radius: 50%;
    background: var(--white);
  }
  .brand-name {
    font-family: "Raleway", sans-serif;
    font-weight: 500;
    font-size: 37px;
    line-height: 1;
    letter-spacing: 1px;
  }
  .brand-tag {
    margin-top: 6px;
    font-size: 8.5px;
    letter-spacing: 1.3px;
    font-weight: 500;
  }

  .date {
    position: absolute;
    right: 164px;
    top: 56px;
    font-family: "Oswald", sans-serif;
    font-weight: 600;
    text-align: right;
    line-height: 0.9;
  }
  .date-day { font-size: 108px; color: var(--gold); letter-spacing: -2px; }
  .date-month { font-size: 66px; color: var(--white); margin-top: 6px; }

  .day-band {
    position: absolute;
    left: 614px; top: 232px;
    width: 50px; height: 270px;
    background: linear-gradient(180deg, rgba(255,255,255,0.28), rgba(255,255,255,0.04));
  }
  .vertical {
    position: absolute;
    transform-origin: left top;
    transform: rotate(-90deg);
    white-space: nowrap;
  }
  .night-name {
    left: 626px; top: 404px;
    font-family: "Oswald", sans-serif;
    font-weight: 500;
    font-size: 24px;
    letter-spacing: 9px;
  }
  .club-floor {
    left: 671px; top: 602px;
    font-family: "Open Sans", sans-serif;
    font-style: italic;
    font-size: 18px;
    letter-spacing: 6.4px;
  }

  .lineup {
    position: absolute;
    left: 0; right: 0; top: 922px;
    text-align: center;
    font-size: 52px;
    line-height: 1;
    color: var(--gold);
    white-space: nowrap;
  }
  .lineup .prefix { font-weight: 300; }
  .lineup .name { font-weight: 800; letter-spacing: -1px; }
  .lineup .amp { font-weight: 500; margin: 0 16px 0 22px; }
  .lineup-rule {
    position: absolute;
    left: 192px; top: 994px;
    width: 472px; height: 4px;
    background: linear-gradient(90deg, rgba(201,203,224,0), var(--mist) 20%, var(--white) 50%, var(--mist) 80%, rgba(201,203,224,0));
  }
  .lineup-note {
    position: absolute;
    left: 0; right: 0; top: 1009px;
    text-align: center;
    font-family: "Open Sans", sans-serif;
    font-style: italic;
    font-size: 17px;
    letter-spacing: 3px;
  }

  .address {
    position: absolute;
    left: 214px; top: 1078px;
    width: 440px; height: 38px;
    border-radius: 19px;
    background: linear-gradient(90deg, var(--gold), var(--gold-deep));
    color: var(--navy-deep);
    font-family: "Josefin Sans", sans-serif;
    font-weight: 700;
    font-size: 15px;
    letter-spacing: 2px;
    text-align: center;
    line-height: 41px;
    white-space: nowrap;
  }
  .website {
    position: absolute;
    left: 0; right: 0; top: 1124px;
    text-align: center;
    font-family: "Open Sans", sans-serif;
    font-style: italic;
    font-size: 16.5px;
    letter-spacing: 0.4px;
    white-space: nowrap;
  }
  .website .highlight { color: var(--gold); }
</style>
</head>
<body>
<main class="flyer">
  <svg class="backdrop" width="856" height="1200" viewBox="0 0 856 1200">
    <defs>
      <linearGradient id="photoTone" x1="0" y1="0" x2="1" y2="1">
        <stop offset="0" stop-color="#2a2450"/>
        <stop offset="0.45" stop-color="#7a2350"/>
        <stop offset="1" stop-color="#2c2a55"/>
      </linearGradient>
      <radialGradient id="smokeRight" cx="0.5" cy="0.5" r="0.5">
        <stop offset="0" stop-color="#d0254c" stop-opacity="0.95"/>
        <stop offset="0.6" stop-color="#a81f45" stop-opacity="0.6"/>
        <stop offset="1" stop-color="#a81f45" stop-opacity="0"/>
      </radialGradient>
      <radialGradient id="smokeLeft" cx="0.5" cy="0.5" r="0.5">
        <stop offset="0" stop-color="#c8234a" stop-opacity="0.8"/>
        <stop offset="1" stop-color="#c8234a" stop-opacity="0"/>
      </radialGradient>
      <linearGradient id="arcEdge" x1="0" y1="1" x2="1" y2="0">
        <stop offset="0" stop-color="#ffffff" stop-opacity="0"/>
        <stop offset="0.5" stop-color="#ffffff" stop-opacity="0.35"/>
        <stop offset="1" stop-color="#ffffff" stop-opacity="0.1"/>
      </linearGradient>
    </defs>
    <rect width="856" height="1200" fill="#1b1a3c"/>
    <ellipse cx="820" cy="640" rx="200" ry="520" fill="url(#smokeRight)"/>
    <ellipse cx="720" cy="1120" rx="260" ry="140" fill="url(#smokeRight)"/>
    <path d="M0 0 H856 V168 C700 560 380 860 0 912 Z" fill="url(#photoTone)" role="img" aria-label="Night city skyline with a DJ listening on headphones, in crimson and navy duotone"/>
    <ellipse cx="90" cy="560" rx="150" ry="150" fill="url(#smokeLeft)"/>
    <path d="M856 168 C700 560 380 860 0 912" fill="none" stroke="url(#arcEdge)" stroke-width="2"/>
  </svg>

  <header class="brand">
    <div class="brand-mark"></div>
    <div class="brand-name">HARBOR</div>
    <div class="brand-tag">NIGHTCLUB + LOUNGE</div>
  </header>

  <div class="date">
    <div class="date-day">1</div>
    <div class="date-month">MAY</div>
  </div>

  <div class="day-band"></div>
  <div class="vertical night-name">FRIDAYS</div>
  <div class="vertical club-floor">DJ VORTAN (CLUB FLOOR)</div>

  <h1 class="lineup">
    <span class="prefix">dj </span><span class="name">RUZO</span><span class="amp">&amp;</span><span class="prefix">dj </span><span class="name">TAV</span>
  </h1>
  <div class="lineup-rule"></div>
  <p class="lineup-note">(residents on the lounge floor)</p>

  <p class="address">4217, MARLOW AVENUE, SACRAMENTO.</p>
  <p class="website">www.harborvenuehall.example for <span class="highlight">list/VIP</span> inquiries</p>
</main>
</body>
</html>
```